kVista Corporate Website

kVista is a well-funded start up developing an Online Marketing Platform for small businesses in Europe.
We are launching in February 2012 with all-in-one online marketing services including professional website, DIY SEO, Dashboard with Reports and Online marketing tools, and Support.
Our internal web designer has come up with a preliminary website design which we wish to continue to improve using new ideas, colours, layout, image, etc.
The brief is very simple - improve the website whether it is look & feel, ease of use, conversion rate - we are looking for overall improvements.
The contest will last 5 days and we will award the winner £300.
If you are the winner , you will also be required to provide designs for 3 more internal pages adhering to the proposed home page design.
Judging criteria : -
Visual Design
Layout must adhere to best practices and wire frame. If you decide to move elements around significantly please provide reason
Functional, informative and drives calls to action
Industry/Entity Type
Marketing
Look and feel
Each slider illustrates characteristics of the customer's brand and the style your logo design should communicate.

```html
<!DOCTYPE html>
<html lang="en">
<head>
<meta charset="utf-8">
<title>kVista – Online Marketing for Small Business</title>
<link href="https://fonts.googleapis.com/css2?family=Open+Sans:wght@400;600&family=Roboto+Condensed:wght@700&family=Arimo:ital,wght@0,400;0,700;1,700&family=Tinos:wght@400;700&display=swap" rel="stylesheet">
<style>
:root{
  --black:#050505;
  --blue-deep:#0a3a78;
  --blue-mid:#1660ad;
  --blue-bright:#1f7fd6;
  --nav-border:#3b93e6;
  --page:#efefef;
  --ink:#222;
  --muted:#555;
  --grey-title:#444;
  --red:#e5252f;
  --navy:#0b3a78;
  --sky:#8fd3f2;
  --peach:#f4bf8c;
  --green:#17822f;
  --mint:#bfe9b8;
  --orange:#f7851f;
  --footer-text:#c9d8ec;
}
*{box-sizing:border-box;margin:0;padding:0}
html,body{width:900px;height:1200px;overflow:hidden;background:#fff}
body{font-family:"Open Sans",sans-serif;color:var(--ink)}
.canvas{position:relative;width:900px;height:1200px;overflow:hidden;background:var(--page)}
.abs{position:absolute}

/* top bar */
.topbar{left:0;top:0;width:900px;height:34px;background:var(--black)}
.account{right:160px;top:10px;color:#fff;font:12px "Arimo",sans-serif;position:absolute}
.account span{margin:0 5px}

/* header */
.hero{left:0;top:34px;width:900px;height:394px;
  background:radial-gradient(ellipse at 50% 55%,var(--blue-bright) 0%,var(--blue-mid) 35%,var(--blue-deep) 100%)}
.brand{left:136px;top:40px;display:flex;align-items:center;gap:8px;color:#fff;font:400 34px "Arimo",sans-serif}
.brand-dot{width:36px;height:36px;border:4px solid #fff;border-radius:50%}
.nav{left:343px;top:51px;height:30px;display:flex;border:1px solid var(--nav-border);background:rgba(10,50,110,.5)}
.nav a{display:flex;align-items:center;padding:0 13px;color:#fff;text-decoration:none;font:700 12px "Arimo",sans-serif;border-left:1px solid var(--nav-border);position:relative}
.nav a:first-child{border-left:none;padding:0 25px}
.nav a.active{background:var(--blue-mid)}
.nav a.active::after{content:"";position:absolute;left:50%;bottom:-1px;margin-left:-5px;border:5px solid transparent;border-bottom-color:#cfe6ff}
.slider{left:123px;top:86px;width:653px;height:307px;background:#1a6fc2;border-radius:4px}
.slide-photo{left:134px;top:98px;width:631px;height:255px;
  background:linear-gradient(100deg,#e9eef3 0%,#cfd9e3 35%,#5a8fc0 60%,#c9d4de 85%,#e6ebef 100%)}
.caption{left:134px;top:353px;width:631px;height:30px;background:rgba(70,70,70,.85);color:#fff;
  font:italic 700 20px "Arimo",sans-serif;text-align:center;line-height:30px;text-shadow:1px 1px 2px #000}
.arrow{top:224px;width:29px;height:36px;background:rgba(110,110,110,.85)}
.arrow.prev{left:134px}.arrow.next{left:736px}
.arrow svg{width:29px;height:36px}
.dots{left:426px;top:404px;display:flex;gap:6px}
.dots i{width:11px;height:11px;border-radius:50%;background:#ddd}
.dots i.on{background:var(--orange)}

/* offers */
.offer{top:456px;width:131px;height:143px;overflow:hidden}
.offer svg{position:absolute;left:0;top:0}
.offer .price{position:absolute;left:6px;top:8px;color:#fff;font:700 27px "Roboto Condensed",sans-serif;line-height:1}
.offer .per{position:absolute;left:6px;top:36px;color:#fff;font:700 13px "Arimo",sans-serif}
.offer .pitch{position:absolute;right:6px;top:64px;text-align:right;color:#333;font:700 19px "Roboto Condensed",sans-serif;line-height:1.05}
.offer .band{position:absolute;left:6px;right:0;bottom:0;height:38px;background:var(--navy);color:#fff;
  font:700 11px "Arimo",sans-serif;display:flex;align-items:center;justify-content:center;text-align:center;line-height:1.1}
.offer .tag{position:absolute;right:-6px;top:14px;width:66px;color:#fff;font:italic 700 11px "Roboto Condensed",sans-serif;text-align:center;transform:rotate(38deg);line-height:1}

/* welcome */
.welcome-title{left:138px;top:612px;font:700 38px "Tinos",serif;color:#333}
.welcome-copy{left:134px;top:660px;width:414px;font-size:10.2px;line-height:13.4px;color:#222}
.btn{display:flex;align-items:center;justify-content:center;background:linear-gradient(#fff,#e9e9e9);border:1px solid #cfcfcf;border-radius:2px;color:#555;font:400 12px "Open Sans",sans-serif}
.examples-title{left:138px;top:780px;font:400 18px "Tinos",serif;color:var(--red)}
.thumb{width:130px;height:91px;background:#cfcfcf;padding:7px}
.thumb div{width:100%;height:100%}
.see-all{left:479px;top:1027px;color:var(--orange);font:400 14px "Arimo",sans-serif}
.divider{left:573px;top:468px;width:1px;height:573px;background:#d4d4d4}

/* sidebar */
.side h3{font:400 24px "Tinos",serif;color:var(--grey-title);line-height:1}
.side p{margin-top:6px;font-size:9.4px;line-height:14px;color:var(--muted);width:170px;letter-spacing:.3px}
.side .btn{margin-top:10px;width:97px;height:26px}

/* footer */
.footer{left:0;top:1058px;width:900px;height:142px;background:radial-gradient(ellipse at 50% 20%,#185da8 0%,#0c3b76 70%,#0a3267 100%)}
.fcol{top:1082px;font-size:10px;line-height:18px;color:var(--footer-text)}
.fsep{top:1084px;width:1px;height:70px;background:rgba(255,255,255,.15)}
.fhead{color:var(--footer-text);font-size:12px}
.email{left:488px;top:1098px;width:132px;height:26px;background:#fff;border:1px solid #aaa;font-size:11px;color:#666;padding:5px 9px}
.signup{left:555px;top:1129px;width:66px;height:22px;background:var(--orange);color:#fff;font-size:12px;text-align:center;line-height:22px;border-radius:2px}
.social{left:661px;top:1102px;display:flex;gap:6px}
.social span{width:25px;height:25px;border-radius:4px;background:#e4e4e4}
.copyright{left:146px;top:1175px;color:#fff;font:400 8px "Arimo",sans-serif}
</style>
</head>
<body>
<div class="canvas">

  <header>
    <div class="abs topbar"></div>
    <div class="account">Login<span>|</span>Register</div>
    <div class="abs hero"></div>
    <div class="abs brand"><span class="brand-dot"></span>kVista</div>
    <nav class="abs nav">
      <a class="active" href="#">HOME</a>
      <a href="#">ABOUT US</a>
      <a href="#">QUICK TOUR</a>
      <a href="#">PRICING</a>
      <a href="#">CONTACT US</a>
    </nav>
    <div class="abs slider"></div>
    <div class="abs slide-photo" role="img" aria-label="Photo of hands typing on a laptop with a glowing world map of web pages above it"></div>
    <div class="abs caption">The Complete Online Marketing for Small Business Websites</div>
    <div class="abs arrow prev"><svg viewBox="0 0 29 36"><path d="M18 10 L11 18 L18 26" stroke="#fff" stroke-width="3" fill="none"/></svg></div>
    <div class="abs arrow next"><svg viewBox="0 0 29 36"><path d="M11 10 L18 18 L11 26" stroke="#fff" stroke-width="3" fill="none"/></svg></div>
    <div class="abs dots"><i></i><i class="on"></i><i></i></div>
  </header>

  <section class="offers">
    <div class="abs offer" style="left:127px">
      <svg width="131" height="143"><rect x="6" y="6" width="125" height="137" fill="var(--sky)"/><polygon points="0,0 100,0 0,100" fill="var(--red)"/></svg>
      <div class="price">£199</div><div class="per" style="font-size:15px">Value</div>
      <div class="pitch" style="font-size:23px;top:48px">Free<br>Setup</div>
      <div class="band" style="font-size:13px">Web offer only</div>
    </div>
    <div class="abs offer" style="left:269px">
      <svg width="131" height="143"><rect x="6" y="6" width="125" height="137" fill="var(--peach)"/><polygon points="0,0 105,0 0,105" fill="var(--navy)"/><polygon points="100,0 131,0 131,60 88,24" fill="var(--red)"/></svg>
      <div class="price">£22</div><div class="per">monthly</div>
      <div class="tag">PRO<br>PACKAGE</div>
      <div class="pitch" style="top:66px">Big Online<br>Presence</div>
      <div class="band">Business Website &amp;<br>Easy Dashboard</div>
    </div>
    <div class="abs offer" style="left:410px">
      <svg width="131" height="143"><rect x="6" y="6" width="125" height="137" fill="var(--mint)"/><polygon points="0,0 105,0 0,105" fill="var(--green)"/><polygon points="100,0 131,0 131,62 86,26" fill="var(--red)"/></svg>
      <div class="price">£29</div><div class="per">monthly</div>
      <div class="tag" style="top:10px">Turbo<br>Sales<br>Pro-Plus</div>
      <div class="pitch" style="top:66px">More<br>Sales Leads</div>
      <div class="band" style="font-size:9.5px">Business Website, Easy<br>Dashboard &amp; PPC Sales</div>
    </div>
  </section>

  <main>
    <h1 class="abs welcome-title">Welcome</h1>
    <p class="abs welcome-copy">kVista will build your business website, optimise SEO marketing and make recommendations on best practices to help you win customers. Let our team of experts design a business website for you. Choose a business website from kVista´s broad array of fabulous, customisable business websites and our experts will have your business online in minutes. kVista lets you create a professional business website without the need to know how to code or programme.</p>
    <a class="abs btn" style="left:461px;top:736px;width:85px;height:26px">Read more</a>

    <h2 class="abs examples-title">View Examples of &nbsp;our Business Websites</h2>
    <div class="abs thumb" style="left:135px;top:813px"><div role="img" aria-label="Green landscape themed website example" style="background:linear-gradient(#eaf1c8,#7fa63a 60%,#f4f4f4 80%)"></div></div>
    <div class="abs thumb" style="left:275px;top:813px"><div role="img" aria-label="Bright blue family themed website example" style="background:linear-gradient(135deg,#1d5fc4,#b9dbf5 50%,#2a7bd6)"></div></div>
    <div class="abs thumb" style="left:414px;top:813px"><div role="img" aria-label="Dark corporate website example" style="background:linear-gradient(#2d2d33,#1a1a1f 40%,#efefef 45%,#efefef 70%,#222 75%)"></div></div>
    <div class="abs thumb" style="left:135px;top:924px"><div role="img" aria-label="Blue and green cartoon landscape website example" style="background:linear-gradient(#1f63c2,#35a3e0 45%,#2ea838 60%,#1d8a29)"></div></div>
    <div class="abs thumb" style="left:275px;top:924px"><div role="img" aria-label="Light green outdoor themed website example" style="background:linear-gradient(#d9ecf9,#f3f7e6 40%,#8cc04a 60%,#f5d64a 90%)"></div></div>
    <div class="abs thumb" style="left:414px;top:924px"><div role="img" aria-label="Blue technology themed website example" style="background:linear-gradient(#e7eef6,#5a8ec9 35%,#f2f4f7 50%,#0f3769 85%)"></div></div>
    <a class="abs see-all">See all &gt;&gt;</a>
  </main>

  <div class="abs divider"></div>

  <aside class="side">
    <div class="abs" style="left:604px;top:472px"><h3>Case Study</h3><p>Read real stories about small businesses online</p><a class="btn">Read more</a></div>
    <div class="abs" style="left:604px;top:583px"><h3>How To</h3><p>Learn from our online marketing tips for small businesses.</p><a class="btn">Learn more</a></div>
    <div class="abs" style="left:604px;top:694px"><h3>News &amp; Chatter</h3><p>Get up-to-date news and chatter about online marketing.</p><a class="btn">Learn more</a></div>
    <div class="abs" style="left:604px;top:805px"><h3>Demo</h3><p>Find out what kVista can do for your business.</p><a class="btn">Find out</a></div>
    <div class="abs" style="left:604px;top:921px"><h3>How does it work?</h3><p>Neque porro quisquam ipsum quia dolor sit amet, consetetur isci velit.</p><a class="btn">Learn more</a></div>
  </aside>

  <footer>
    <div class="abs footer"></div>
    <div class="abs fcol" style="left:146px">Home<br>Quick Tour<br>Pricing<br>Contact Us</div>
    <div class="abs fsep" style="left:218px"></div>
    <div class="abs fcol" style="left:230px">Search Marketing<br>Organic/Natural (SEO)<br>Social Media<br>Web Analytics</div>
    <div class="abs fsep" style="left:344px"></div>
    <div class="abs fcol" style="left:362px;top:1081px;line-height:20px">Sitemap<br>Terms &amp; Conditions</div>
    <div class="abs fsep" style="left:470px"></div>
    <div class="abs fhead" style="left:492px;top:1080px">Newsletter Sign-up</div>
    <div class="abs email">Email Address</div>
    <div class="abs signup">Sign Up</div>
    <div class="abs fsep" style="left:638px"></div>
    <div class="abs fhead" style="left:661px;top:1082px">Follow Us</div>
    <div class="abs social" aria-label="Social network links"><span></span><span></span><span></span></div>
    <div class="abs copyright">kVista PVT Ltd. &nbsp;© 2012 &nbsp;| &nbsp;All Rights Reserved</div>
  </footer>

</div>
</body>
</html>
```